Handy man Company business card

need branded business card for my new company, this design will transfer to car wrap design what winner will be asked to design

I will need original file so I can edit it in the end.

Also like to have some inspirational quote like "ONE CALL WE DO IT ALL"
"We do it right" can be added to logo side

Like to try to see large 1 800 000 0000 number on front with large logo

Size bigger then standard business card

I like to integrate LAS VEGAS sign to one of sides

Target Market(s)

Handy man services, Home renovation and remodeling

Industry/Entity Type

Handyman

Contact Information for Business Card

Tool Baron LLC.
Name: BORIS LENKOVA
Phone "Temporary": 000 000 0000
Adress: 2715 Fenmore Ct, Las Vegas NV 89147
Website: www.toolbaron.vegas
Email: info@toolbaron.vegas

Requirements
Must have
• Two side
• side n1: LOGO
• side n2: INFO
Nice to have
• Like to have some interesting idea for client to remember!
• With logo added to both side at different stile
Should not have
• Standard design,

```html
<!DOCTYPE html>
<html lang="en">
<head>
<meta charset="utf-8">
<title>Tool Baron — Business Card</title>
<link rel="stylesheet" href="https://fonts.googleapis.com/css2?family=Open+Sans:wght@400;600&display=swap">
<style>
  :root {
    --stage: #d9d9d9;
    --card-dark: #1a2b38;
    --card-mid: #2a3e4c;
    --text-light: #ffffff;
    --accent: #f2b324;
    --mascot-warm: #f0b040;
    --mascot-cool: #7fb8d8;
  }
  * { margin: 0; padding: 0; box-sizing: border-box; }
  html, body {
    width: 1200px;
    height: 1200px;
    overflow: hidden;
    background: var(--stage);
    font-family: "Open Sans", Arial, sans-serif;
  }
  .stage {
    width: 1200px;
    height: 1200px;
    display: flex;
    align-items: center;
    justify-content: center;
  }
  .card-front {
    position: relative;
    width: 1000px;
    height: 580px;
    background: linear-gradient(160deg, var(--card-mid) 0%, var(--card-dark) 55%, var(--card-dark) 100%);
    color: var(--text-light);
  }
  .brand {
    position: absolute;
    left: 70px;
    bottom: 90px;
    display: flex;
    align-items: flex-end;
    gap: 22px;
  }
  .brand-mascot {
    width: 86px;
    height: 110px;
    border-radius: 10px;
    background: linear-gradient(180deg, var(--mascot-warm) 0%, var(--mascot-cool) 55%, var(--mascot-warm) 100%);
  }
  .brand-name {
    font-size: 72px;
    font-weight: 400;
    line-height: 1;
    letter-spacing: 0.5px;
    color: var(--text-light);
  }
  .contact {
    position: absolute;
    right: 60px;
    top: 60px;
    text-align: right;
  }
  .contact-name {
    font-size: 36px;
    font-weight: 400;
    letter-spacing: 1px;
    margin-bottom: 26px;
    margin-right: 58px;
  }
  .contact-list { list-style: none; }
  .contact-item {
    display: flex;
    align-items: center;
    justify-content: flex-end;
    gap: 22px;
    font-size: 26px;
    line-height: 1;
    height: 36px;
    margin-bottom: 12px;
  }
  .contact-icon {
    width: 32px;
    height: 32px;
    background: var(--accent);
    display: flex;
    align-items: center;
    justify-content: center;
    flex: none;
  }
  .contact-icon svg { width: 20px; height: 20px; }
</style>
</head>
<body>
<main class="stage">
  <section class="card-front">
    <div class="brand">
      <div class="brand-mascot" role="img" aria-label="Cartoon handyman mascot in cap and overalls"></div>
      <span class="brand-name">Tool Baron</span>
    </div>

    <div class="contact">
      <p class="contact-name">BORIS LENKOVA</p>
      <ul class="contact-list">
        <li class="contact-item">
          <span>000 000 0000</span>
          <span class="contact-icon">
            <svg viewBox="0 0 24 24" aria-hidden="true"><path fill="#1a2b38" d="M6.6 10.8a15 15 0 0 0 6.6 6.6l2.2-2.2a1 1 0 0 1 1-.25 11.4 11.4 0 0 0 3.6.57 1 1 0 0 1 1 1V20a1 1 0 0 1-1 1A17 17 0 0 1 3 4a1 1 0 0 1 1-1h3.5a1 1 0 0 1 1 1c0 1.25.2 2.45.57 3.57a1 1 0 0 1-.25 1z"/></svg>
          </span>
        </li>
        <li class="contact-item">
          <span>www.toolbaron.vegas</span>
          <span class="contact-icon">
            <svg viewBox="0 0 24 24" aria-hidden="true"><g fill="none" stroke="#1a2b38" stroke-width="2"><circle cx="12" cy="12" r="9"/><ellipse cx="12" cy="12" rx="4" ry="9"/><path d="M3 12h18"/></g></svg>
          </span>
        </li>
        <li class="contact-item">
          <span>info@toolbaron.vegas</span>
          <span class="contact-icon">
            <svg viewBox="0 0 24 24" aria-hidden="true"><g fill="none" stroke="#1a2b38" stroke-width="2"><rect x="3" y="5" width="18" height="14"/><path d="M3 5l9 8 9-8"/></g></svg>
          </span>
        </li>
        <li class="contact-item">
          <span>2715 Fenmore Ct, Las Vegas NV 89147</span>
          <span class="contact-icon">
            <svg viewBox="0 0 24 24" aria-hidden="true"><path fill="#1a2b38" d="M12 2a7 7 0 0 0-7 7c0 5 7 13 7 13s7-8 7-13a7 7 0 0 0-7-7zm0 9.5A2.5 2.5 0 1 1 12 6.5a2.5 2.5 0 0 1 0 5z"/></svg>
          </span>
        </li>
      </ul>
    </div>
  </section>
</main>
</body>
</html>
```